Business Card Design

We would like a business card that utilizes our current logo and keeps with the same feel - elegant and organic. Our farm isn't about mass production, it's about excellence, education, beautiful events and flowers - people, culture, and community.

Target Market(s)

Patrons to our farm who are interested in weddings, events, or our flowers and vegetables.

Contact Information for Business Card

Name, address, cell email (Danielle Hoskins, 2716 Wrenfield Rd, Millbrook, CO 80547, cell 30.412.6638, email danielle@wrenfieldacres.com)

```html
<!DOCTYPE html>
<html lang="en">
<head>
<meta charset="utf-8">
<title>Wrenfield Acres – Business Card</title>
<link href="https://fonts.googleapis.com/css2?family=Urbanist:wght@400;700&display=swap" rel="stylesheet">
<style>
  :root {
    --page-bg: #ffffff;
    --card-sage: #778a76;
    --ink-white: #ffffff;
    --name-tan: #a6825f;
    --name-edge: #4a3b2c;
  }
  html, body {
    margin: 0;
    width: 1200px;
    height: 900px;
    overflow: hidden;
    background: var(--page-bg);
    font-family: "Urbanist", sans-serif;
  }
  .canvas {
    position: relative;
    width: 1200px;
    height: 900px;
  }
  .business-card {
    position: absolute;
    left: 318px;
    top: 273px;
    width: 568px;
    height: 357px;
    border-radius: 17px;
    background: var(--card-sage);
    box-shadow: 0 8px 28px rgba(0, 0, 0, 0.14);
    color: var(--ink-white);
  }
  .brand-name {
    position: absolute;
    left: 0;
    right: 0;
    top: 60px;
    margin: 0;
    text-align: center;
    font-weight: 400;
    font-size: 44px;
    letter-spacing: 1px;
    color: var(--ink-white);
  }
  .person-name {
    position: absolute;
    left: 0;
    right: 0;
    top: 157px;
    margin: 0;
    text-align: center;
    font-weight: 700;
    font-size: 48px;
    line-height: 60px;
    letter-spacing: 0.5px;
    color: var(--name-tan);
    -webkit-text-stroke: 1px var(--name-edge);
    text-shadow:
      1.5px 0 0 var(--ink-white), -1.5px 0 0 var(--ink-white),
      0 1.5px 0 var(--ink-white), 0 -1.5px 0 var(--ink-white),
      1px 1px 0 var(--ink-white), -1px -1px 0 var(--ink-white),
      1px -1px 0 var(--ink-white), -1px 1px 0 var(--ink-white);
  }
  .contact-list {
    position: absolute;
    left: 31px;
    top: 229px;
    margin: 0;
    padding: 0;
    list-style: none;
  }
  .contact-item {
    display: flex;
    align-items: center;
    height: 26px;
    margin-bottom: 14px;
    font-size: 23px;
    font-weight: 400;
    white-space: nowrap;
  }
  .contact-icon {
    width: 26px;
    height: 26px;
    margin-right: 10px;
    flex: none;
  }
</style>
</head>
<body>
<main class="canvas">
  <section class="business-card">
    <h1 class="brand-name">Wrenfield Acres</h1>
    <h2 class="person-name">Danielle Hoskins</h2>
    <ul class="contact-list">
      <li class="contact-item">
        <svg class="contact-icon" viewBox="0 0 26 26" aria-hidden="true">
          <rect width="26" height="26" rx="4" fill="#fff"/>
          <path d="M13 4.5c-3.6 0-6.3 2.7-6.3 6.2 0 4.4 6.3 10.8 6.3 10.8s6.3-6.4 6.3-10.8c0-3.5-2.7-6.2-6.3-6.2z" fill="#778a76"/>
          <circle cx="13" cy="10.6" r="2.3" fill="#fff"/>
        </svg>
        <span>2716 Wrenfield Rd, Millbrook, CO 80547</span>
      </li>
      <li class="contact-item">
        <svg class="contact-icon" viewBox="0 0 26 26" aria-hidden="true">
          <rect width="26" height="26" rx="4" fill="#fff"/>
          <path d="M8.2 5.5l2.6-.4 1.6 3.9-1.8 1.4c.9 2 2.5 3.6 4.5 4.6l1.4-1.8 3.9 1.6-.4 2.6c-.2 1-1.1 1.7-2.1 1.6C11.8 18.5 7.5 14.2 7 8.1c-.1-1 .4-2.4 1.2-2.6z" fill="#778a76"/>
        </svg>
        <span>30.412.6638</span>
      </li>
      <li class="contact-item">
        <svg class="contact-icon" viewBox="0 0 26 26" aria-hidden="true">
          <rect width="26" height="26" rx="4" fill="#fff"/>
          <rect x="4.5" y="7.5" width="17" height="11" fill="none" stroke="#778a76" stroke-width="1.6"/>
          <path d="M4.5 7.5l8.5 6.5 8.5-6.5M4.5 18.5l6.2-5.5M21.5 18.5l-6.2-5.5" fill="none" stroke="#778a76" stroke-width="1.4"/>
        </svg>
        <span>danielle@wrenfieldacres.com</span>
      </li>
    </ul>
  </section>
</main>
</body>
</html>
```